Business Card Design for Portrait photography professional

We are a small company specializing in portrait photography (weddings, family, couples, children, newborn, pregnant, etc.) Occasionally we do business portraits too and do some other type of photography. We need a business card which would fit into the same look and feel as our website theme (lumvika.com - under construction currently).
Our target customer base lies within mid- to upmarket. We want our business cards to convey a feeling of quality, solidness and a bit luxury.
Design should be universal and usable on 85mmx55mm, 90mmx50mm and 90mmx55mm
one extra file (PSD of a website didn't fit into the allowed updoad, therefore has put it into my filecrate: https://www.filecrate-example.net/s/qt7wk2rbvx9dmhe/website%20theme%20PSD.psd)

Target Market(s)

mostly private people, 25-60 years old, mostly well established.

Industry/Entity Type

Portrait Photography

Requirements
Must have
• 2 sided design (print on both sides of the business card).
Must include:
business name, logo, URL (lumvika.no) , employee name, email address, and phone number.
Colorscheme of the website lumvika.no / lumvika.com

```html
<!DOCTYPE html>
<html lang="en">
<head>
<meta charset="utf-8">
<title>Lumvika – Business Card</title>
<link rel="stylesheet" href="https://fonts.googleapis.com/css2?family=Marcellus&display=swap">
<style>
  :root {
    --canvas: #e9e5df;
    --card: #050505;
    --ink: #f4f2ee;
    --ink-soft: #d9d6d0;
    --shadow: rgba(0, 0, 0, 0.45);
  }
  * { margin: 0; padding: 0; box-sizing: border-box; }
  html, body {
    width: 1200px;
    height: 1000px;
    overflow: hidden;
    background: var(--canvas);
  }
  .canvas {
    position: relative;
    width: 1200px;
    height: 1000px;
  }
  .card {
    position: absolute;
    top: 350px;
    width: 535px;
    height: 300px;
    background: var(--card);
    border-radius: 10px;
    box-shadow: 0 6px 14px var(--shadow);
    color: var(--ink);
    font-family: "Marcellus", Georgia, serif;
  }
  .card--front { left: 48px; }
  .card--back { left: 618px; }

  .brand {
    position: absolute;
    display: flex;
    align-items: center;
    gap: 12px;
    font-size: 30px;
    color: var(--ink);
    white-space: nowrap;
  }
  .brand__dot {
    width: 18px;
    height: 18px;
    border-radius: 50%;
    background: var(--ink);
  }
  .card--front .brand { left: 40px; top: 132px; }
  .card--back .brand { left: 50%; top: 120px; transform: translateX(-50%); }

  .divider {
    position: absolute;
    left: 266px;
    top: 12px;
    width: 3px;
    height: 276px;
    background: linear-gradient(to bottom, transparent 0%, rgba(255,255,255,0.9) 50%, transparent 100%);
  }

  .employee-name {
    position: absolute;
    left: 325px;
    top: 62px;
    font-size: 20px;
    font-weight: 400;
  }

  .contact-list {
    position: absolute;
    left: 320px;
    top: 190px;
    list-style: none;
  }
  .contact-list li {
    display: flex;
    align-items: center;
    gap: 8px;
    height: 25px;
    font-size: 12px;
    color: var(--ink-soft);
  }
  .contact-icon { width: 15px; height: 15px; flex: none; }

  .tagline {
    position: absolute;
    left: 0;
    right: 0;
    top: 231px;
    text-align: center;
    font-size: 15px;
    letter-spacing: 0.2px;
  }
</style>
</head>
<body>
<main class="canvas">

  <section class="card card--front" aria-label="Business card front">
    <div class="brand"><span class="brand__dot"></span>lumvika.no</div>
    <div class="divider"></div>
    <h1 class="employee-name">Employee Name</h1>
    <ul class="contact-list">
      <li>
        <svg class="contact-icon" viewBox="0 0 16 16" aria-hidden="true">
          <circle cx="8" cy="8" r="7.5" fill="#f4f2ee"/>
          <path d="M5.3 4.2l1.3 1.6-.7.9c.5 1.1 1.3 1.9 2.4 2.4l.9-.7 1.6 1.3-.9 1.3c-2.6-.4-4.6-2.4-5-5z" fill="#050505"/>
        </svg>
        0123 456 789
      </li>
      <li>
        <svg class="contact-icon" viewBox="0 0 16 16" aria-hidden="true">
          <circle cx="8" cy="8" r="7.5" fill="#f4f2ee"/>
          <rect x="4" y="5.3" width="8" height="5.6" fill="#050505"/>
          <path d="M4 5.3l4 3.2 4-3.2" fill="none" stroke="#f4f2ee" stroke-width="0.8"/>
        </svg>
        email.address@lumvika.no
      </li>
      <li>
        <svg class="contact-icon" viewBox="0 0 16 16" aria-hidden="true">
          <circle cx="8" cy="8" r="7.5" fill="#f4f2ee"/>
          <g fill="none" stroke="#050505" stroke-width="0.9">
            <circle cx="8" cy="8" r="4.5"/>
            <ellipse cx="8" cy="8" rx="2" ry="4.5"/>
            <path d="M3.5 8h9M4.2 5.7h7.6M4.2 10.3h7.6"/>
          </g>
        </svg>
        www.lumvika.no
      </li>
    </ul>
  </section>

  <section class="card card--back" aria-label="Business card back">
    <div class="brand"><span class="brand__dot"></span>lumvika.no</div>
    <p class="tagline">PERSONAL PHOTOGRAPHER</p>
  </section>

</main>
</body>
</html>
```